Flier Template in Microsoft Word

We need to a have a flier about farm practices developed in Microsoft Word. Each farm will able to add their own logos and photos. We will give them a model that they can customize.

We want a traditional "country" flavor. Green colors and earth tones are best. Please use the photos we have provided.

The final product must be in Microsoft Word for our farmers to customize.
Updates

All designers: Please have a white background (maybe with a watermark). Our client will print these on white paper using a desktop printer. Thank you!

Target Market(s)

People who shop at Farmer's Markets, join CSAs, and enjoy cooking with fresh vegetables.

Industry/Entity Type

Farm

Font styles to use
Serif

Requirements
Must have
• Must use the text and general layout of the Microsoft Word document attached
Must use the pictures we provided.
Final product must be in Microsoft Word
Must be able to easily swap out the logo at the top
Must be able to print on white paper on a desktop printer
Nice to have
• A nice header that looks like a farm or food on the table
A nice watermark or background to make the flier look polished
Should not have
• Do not change the photos
Do not use high tech fonts or graphic treatments

```html
<!DOCTYPE html>
<html lang="en">
<head>
<meta charset="utf-8">
<title>Sustainable Grazing – Fresh Roots Series Flier</title>
<link href="https://fonts.googleapis.com/css2?family=Arimo:ital,wght@0,400;0,700;1,400&family=Carlito:wght@400;700&family=Gelasio:ital,wght@0,400;0,700;1,400&display=swap" rel="stylesheet">
<style>
  :root {
    --backdrop: #1b1512;
    --paper: #ffffff;
    --green: #3f8a1c;
    --green-dark: #2f6b12;
    --rule: #5aa02c;
    --frame: #6bb23a;
    --ink: #1e1e1e;
    --brown: #7a3d12;
    --sans: "Arimo", Arial, sans-serif;
    --body: "Carlito", Calibri, sans-serif;
    --serif: "Gelasio", Georgia, serif;
  }
  * { box-sizing: border-box; margin: 0; padding: 0; }
  html, body { width: 1200px; height: 927px; overflow: hidden; background: var(--backdrop); }
  .canvas { position: relative; width: 1200px; height: 927px; background: var(--backdrop); }

  .page { position: absolute; width: 503px; background: var(--paper); color: var(--ink); }
  .page--front { left: 89px; top: 80px; height: 661px; }
  .page--back { left: 613px; top: 172px; height: 660px; }
  .page > * { position: absolute; }

  /* header band */
  .masthead { left: 17px; top: 16px; width: 469px; height: 82px;
    background: linear-gradient(180deg, #b9d3ea 0%, #d9e6ef 30%, #7f9a63 55%, #5f8640 75%, #a5782f 100%); }
  .masthead__logo { position: absolute; left: 4px; top: 24px; width: 57px; height: 52px; background: var(--paper);
    border: 2px solid var(--frame); border-radius: 7px; display: flex; align-items: center; justify-content: center;
    text-align: center; font-family: var(--body); font-size: 9px; line-height: 11px; }
  .masthead__strip { position: absolute; left: 0; bottom: 0; width: 100%; height: 14px; background: var(--green);
    color: #fff; font-family: var(--serif); font-size: 9px; line-height: 14px; padding-left: 72px; white-space: nowrap; }
  .masthead__strip b { font-size: 11px; }
  .masthead__strip i { margin-left: 4px; }

  .title { left: 0; top: 118px; width: 100%; text-align: center; font-family: var(--sans); font-weight: 700;
    font-size: 14px; color: var(--green); }
  .subtitle { left: 0; top: 136px; width: 100%; text-align: center; font-family: var(--serif); font-style: italic;
    font-size: 11px; color: var(--green); }

  .heading { display: flex; align-items: center; gap: 6px; font-family: var(--sans); font-weight: 700; color: var(--green); }
  .heading svg { width: 12px; height: 10px; flex: none; }
  .heading--lg { font-size: 13px; }
  .heading--md { font-size: 11.5px; }

  .copy { font-family: var(--body); font-size: 9.4px; line-height: 12.2px; text-align: justify; }

  .photo { border: 2px solid var(--frame); }
  .caption { font-family: var(--body); font-weight: 700; font-size: 8px; color: var(--brown); }

  /* back page rows */
  .row-text { left: 200px; width: 280px; font-family: var(--serif); font-size: 9.6px; line-height: 12px; text-align: justify; }
  .row-rule { left: 200px; width: 277px; height: 3px; background: var(--rule); }

  .footer-mark { left: 22px; top: 584px; display: flex; align-items: center; gap: 4px;
    font-family: var(--body); font-size: 7px; font-weight: 700; color: var(--green-dark); width: 80px; line-height: 8px; }
  .footer-mark span.dot { width: 14px; height: 14px; border-radius: 50%; background: #b8dc8c; flex: none; }
  .footer-copy { left: 104px; top: 584px; width: 340px; font-family: var(--body); font-size: 9.4px; line-height: 12.5px; }
  .footer-copy b { color: var(--green); }
</style>
</head>
<body>
<div class="canvas">

  <!-- Front page -->
  <section class="page page--front">
    <div class="masthead" role="img" aria-label="Panorama of green hills, fields and a small valley town under a blue sky">
      <div class="masthead__logo">Your<br>logo<br>here</div>
      <div class="masthead__strip"><b>The Fresh Roots Series</b> &nbsp;| &nbsp;<i>A Healthier Environment, One Meal at a Time</i></div>
    </div>

    <h1 class="title">SUSTAINABLE GRAZING</h1>
    <p class="subtitle">Happier Cows = Healthier Milk and Cleaner Streams</p>

    <h2 class="heading heading--lg" style="left:17px;top:164px;">
      <svg viewBox="0 0 12 10"><path d="M1 3.5h6V1l4 4-4 4V6.5H1z" fill="none" stroke="#8cc63f" stroke-width="1"/></svg>Who We Are</h2>
    <p class="copy" style="left:28px;top:188px;width:458px;">Maple Hollow Dairy Farm is a third generation dairy farm located on 64 acres in the Willow Creek Valley. We raise holsteins to produce milk and also raise hens for eggs. We sell much of our milk, as well as cheese, yogurt and baked goods directly from the farm.</p>

    <h2 class="heading heading--md" style="left:17px;top:240px;">
      <svg viewBox="0 0 12 10"><path d="M1 3.5h6V1l4 4-4 4V6.5H1z" fill="none" stroke="#8cc63f" stroke-width="1"/></svg>What Have We Done</h2>
    <p class="copy" style="left:28px;top:265px;width:242px;">At Maple Hollow Dairy Farm, we take care of our animals and our animals help us take care of the land. Corn and other grains are not a natural part of a cows’ diet, so we don’t feed them that. Instead, we let them roam the pastures eating grass and other plants. We move the cows from pasture to pasture on a thoughtful schedule to prevent overgrazing, and this reduces soil erosion and water pollution. Our animals are happier and our land and water is healthier.</p>
    <div class="photo" style="left:280px;top:242px;width:200px;height:157px;background:linear-gradient(180deg,#9fb58a 0%,#6f8f4e 45%,#4c8a2a 70%,#3f7a22 100%);" role="img" aria-label="Farmer standing in front of a red tractor in a green field"></div>

    <h2 class="heading heading--md" style="left:17px;top:389px;">
      <svg viewBox="0 0 12 10"><path d="M1 3.5h6V1l4 4-4 4V6.5H1z" fill="none" stroke="#8cc63f" stroke-width="1"/></svg>When and Where We Did It</h2>
    <p class="copy" style="left:28px;top:412px;width:458px;">In 2010, we had our cows in a stall barn and corn or soybeans in our fields. We looked into switching some of our acreage from crops to pasture and soon realized that it would beneficial to our cows and our soil. We then installed fencing to divide the fields into smaller paddocks and in spring 2011, we planted a seed mixture containing plants that provide the nutrition our cows need and that provides support for the soil.</p>

    <div class="photo" style="left:28px;top:473px;width:222px;height:141px;background:linear-gradient(180deg,#b7cde4 0%,#8a9a8c 30%,#7d9a4a 55%,#6b6a45 100%);" role="img" aria-label="Before: cattle grazing beside an eroded stream bank"></div>
    <div class="photo" style="left:254px;top:473px;width:225px;height:141px;background:linear-gradient(180deg,#c2d6ea 0%,#93a89a 30%,#6f9a3c 55%,#5a7f2a 100%);" role="img" aria-label="After: fenced stream with grassy, restored banks"></div>
    <p class="caption" style="left:28px;top:622px;">BEFORE</p>
    <p class="caption" style="left:254px;top:622px;">AFTER</p>
  </section>

  <!-- Back page -->
  <section class="page page--back">
    <h2 class="heading heading--md" style="left:20px;top:28px;">
      <svg viewBox="0 0 12 10"><path d="M1 3.5h6V1l4 4-4 4V6.5H1z" fill="none" stroke="#8cc63f" stroke-width="1"/></svg>Why You Should Care</h2>
    <p class="copy" style="left:25px;top:50px;width:452px;">At Maple Hollow Dairy Farm, we believe that the care of land and water contributes to the care and safety of your family. When you buy from Maple Hollow Dairy Farm, you are helping us to do our part to make clean, healthy food available to you without harm to the environment.</p>

    <div class="photo" style="left:25px;top:116px;width:157px;height:101px;background:linear-gradient(135deg,#6d8d5a 0%,#b04a3a 45%,#d8b24a 70%,#8aa0b6 100%);" role="img" aria-label="Farmers market stand with fresh produce"></div>
    <p class="row-text" style="top:150px;">Fresh and locally produced food from our farm tastes better, and it’s better for our local economy and environment.</p>
    <div class="row-rule" style="top:212px;"></div>

    <div class="photo" style="left:25px;top:225px;width:157px;height:97px;background:linear-gradient(135deg,#e0c39a 0%,#c98a55 45%,#6ea33a 75%,#c93b2a 100%);" role="img" aria-label="Parent and child preparing fresh vegetables in a kitchen"></div>
    <p class="row-text" style="top:264px;">Fresh food is healthier for kids of all ages than processed food.</p>
    <div class="row-rule" style="top:321px;"></div>

    <div class="photo" style="left:25px;top:332px;width:157px;height:93px;background:linear-gradient(180deg,#8fb3cf 0%,#6f8c7a 40%,#5a4a3c 70%,#3c6a2a 100%);" role="img" aria-label="Family holding a freshly caught fish by a lake"></div>
    <p class="row-text" style="top:357px;">As a result of the improvements described here, the waterways that run through our farm are cleaner, benefitting everyone downstream.</p>
    <div class="row-rule" style="top:421px;"></div>

    <div class="photo" style="left:25px;top:433px;width:157px;height:94px;background:linear-gradient(180deg,#7a6a55 0%,#9c8a70 40%,#5f7f8f 75%,#3f5f70 100%);" role="img" aria-label="Bird of prey catching a fish above the water"></div>
    <p class="row-text" style="top:469px;">Our wildlife neighbors appreciate the cleaner waterways even more than you do!</p>
    <div class="row-rule" style="top:522px;"></div>

    <div class="footer-mark"><span class="dot"></span>Riverbend Conservation Council</div>
    <p class="footer-copy"><b>Riverbend Conservation Council’s Fresh Roots Series</b> promotes local farms that produce fresh, high quality, healthy foods using farm practices that keep our water clean and our families safe.</p>
  </section>

</div>
</body>
</html>
```